Business Card Design Project

I need some business cards with the logo you did for us (attached)
I am looking for a coulourful yet serious business card

We do market research
on the back I want the logo

on the front my name : Corinne Valdessac
position : Manager
address : Brume Analytica Sarl - 27 Rue des tanneurs
1847 Glarency - Switzerland
corinne.valdessac@brumeanalytica.ch
Tel : +4122 934 07 58
Mob France :+33 671 42 8356
Mob Italy +39 347 520 8163

The tree of the logo could also be used alone

THE BACKGROUND COLOR ON THE FRONT HAS TO BE WHITE, ON THE BACK YU CAN TRY OHER COLOUR BUT HOMOGENEOUS (NOT EXPENSIVE TO PRINT)

Target Market(s)

multinational companies or other market research companies

Industry/Entity Type

Market Research

Requirements
Must have
• logo on the back
and all the info above

```html
<!DOCTYPE html>
<html lang="en">
<head>
<meta charset="utf-8">
<title>Brume Analytica – Business Card</title>
<link href="https://fonts.googleapis.com/css2?family=Open+Sans:wght@400;600;700&display=swap" rel="stylesheet">
<style>
  :root {
    --stage: #ecebe7;
    --green-light: #a6cf3f;
    --green-mid: #8cbc2c;
    --green-deep: #6fa01c;
    --green-tone: #86b52a;
    --paper: #ffffff;
    --brand: #b3174a;
    --ink-dark: #2f3a16;
    --ink-body: #4a5235;
  }
  * { box-sizing: border-box; margin: 0; padding: 0; }
  html, body { width: 1200px; height: 723px; overflow: hidden; }
  body {
    background: var(--stage);
    font-family: "Open Sans", sans-serif;
    display: flex;
    align-items: center;
    justify-content: center;
    gap: 80px;
  }
  .card {
    width: 380px;
    height: 600px;
    position: relative;
    overflow: hidden;
    box-shadow: 0 6px 18px rgba(0,0,0,0.18);
  }

  /* Back: one homogeneous colour */
  .card--back { background: var(--green-mid); }
  .card--back .back-name {
    position: absolute;
    left: 0; right: 0;
    top: 250px;
    text-align: center;
    color: var(--green-deep);
    font-weight: 600;
    font-size: 34px;
  }
  .card--back .website {
    position: absolute;
    left: 0; right: 0;
    bottom: 48px;
    text-align: center;
    color: var(--brand);
    font-weight: 700;
    font-size: 20px;
    letter-spacing: 0.18em;
  }

  /* Front: white background, green accents */
  .card--front { background: var(--paper); }
  .brand-panel {
    height: 190px;
    display: flex;
    align-items: center;
    justify-content: center;
    gap: 14px;
  }
  .brand-dot {
    width: 26px;
    height: 26px;
    border-radius: 50%;
    background: var(--brand);
  }
  .brand-name {
    color: var(--brand);
    font-weight: 600;
    font-size: 36px;
  }
  .divider {
    height: 9px;
    margin: 0 24px;
    border-top: 3px solid var(--green-mid);
    border-bottom: 3px solid var(--green-mid);
  }
  .details {
    padding: 44px 24px 0;
    text-align: center;
    color: var(--ink-body);
    font-size: 15px;
    line-height: 1.45;
  }
  .person-name { font-weight: 700; font-size: 20px; color: var(--green-deep); }
  .person-role { font-weight: 700; font-size: 13px; color: var(--ink-dark); margin-bottom: 28px; }
  .address { margin-bottom: 28px; }
  .email { color: var(--brand); font-weight: 700; font-size: 14px; }
  .foot-band {
    position: absolute;
    left: 0; right: 0; bottom: 0;
    height: 14px;
    background: var(--green-mid);
  }
</style>
</head>
<body>
  <section class="card card--back">
    <p class="back-name">brume analytica</p>
    <p class="website">www.brumeanalytica.ch</p>
  </section>

  <section class="card card--front">
    <header class="brand-panel">
      <span class="brand-dot"></span>
      <span class="brand-name">brume analytica</span>
    </header>
    <div class="divider"></div>
    <div class="details">
      <p class="person-name">Corinne Valdessac</p>
      <p class="person-role">Manager</p>
      <p class="address">Brume Analytica Sarl - 27 Rue des tanneurs<br>1847 Glarency - Switzerland</p>
      <p class="phones">PH: +4122 934 07 58<br>Mob France: +33 671 42 8356<br>Mob Italy: +39 347 520 8163</p>
      <p class="email">corinne.valdessac@brumeanalytica.ch</p>
    </div>
    <div class="foot-band"></div>
  </section>
</body>
</html>
```